Atelier Vane Architecture business card

We need to update our business card. We do high end custom residential, hospitality, and wellness architecture. We focus on creating unique spaces and design around the five senses, believing that architecture's true impact is not on our surroundings, but within us. We would like to see designs are instill a sense of calm awe. They should be crisp, fresh, clean, authentic, & contemporary without being sterile, overworked, or harsh. White space is important. Alternative materials are an option if natural. We have created our own logo and would like designs to incorporate it. However, we are willing to see alternatives if the logo becomes a stumbling block and you have an alternate you suggest. Card must have the following information:
Atelier Vane Architecture, Inc.
742 Marbury Rd. NE Atlanta, GA 30319
Dominic K. Whitlow, AIA, NCARB, LEED AP BD+C
ateliervane.example

Target Market(s)

Higher net worth individuals with an appreciation for design, nature, sustainability,

Industry/Entity Type

Architect

Contact Information for Business Card

See above. The title of Owner or Architect is helpful but not necessary. Minimalism should trump additional information.

Font styles to use
Serif
Sans Serif

Requirements
Must have
• It should look professional. It must use logo
Should not have
• caligraphy, animals, anything that is cute,

```html
<!DOCTYPE html>
<html lang="en">
<head>
<meta charset="utf-8">
<title>Atelier Vane Architecture — Business Card</title>
<link rel="stylesheet" href="https://fonts.googleapis.com/css2?family=Open+Sans:wght@400;600&display=swap">
<style>
  :root {
    --brand-green: #06760f;
    --brand-green-soft: #2f8f37;
    --paper: #ffffff;
    --backdrop: #ece8e4;
    --ink-light: #ffffff;
  }
  * { box-sizing: border-box; margin: 0; padding: 0; }
  html, body { width: 1200px; height: 900px; overflow: hidden; }
  body {
    position: relative;
    background: var(--backdrop);
    font-family: "Open Sans", Arial, sans-serif;
  }
  .card {
    position: absolute;
    background: var(--paper);
    overflow: hidden;
    box-shadow: 0 6px 18px rgba(0,0,0,0.18);
  }
  /* Front */
  .card-front { left: 77px; top: 34px; width: 589px; height: 363px; }
  .card-front .front-header { position: absolute; inset: 0 0 auto 0; height: 153px; }
  .card-front .front-panel {
    position: absolute; left: 0; right: 0; bottom: 0; height: 210px;
    background: var(--brand-green); color: var(--ink-light);
  }
  .brand-name {
    position: absolute;
    display: flex; align-items: center; gap: 10px;
    color: var(--brand-green);
    font-weight: 600;
    letter-spacing: 0.04em;
    white-space: nowrap;
  }
  .brand-mark {
    width: 14px; height: 14px; border-radius: 50%;
    background: var(--brand-green);
  }
  .card-front .brand-name { left: 34px; top: 58px; font-size: 20px; }
  .contact-name { position: absolute; left: 34px; top: 20px; font-size: 19px; font-weight: 600; }
  .contact-credentials { position: absolute; left: 34px; top: 44px; font-size: 15px; }
  .contact-list { position: absolute; left: 34px; top: 75px; list-style: none; font-size: 15px; line-height: 21px; }
  .contact-list li { display: flex; align-items: center; gap: 9px; }
  .contact-list svg { width: 12px; height: 12px; fill: var(--ink-light); }
  .contact-address { position: absolute; left: 30px; top: 158px; font-size: 15px; }
  .panel-accent {
    position: absolute; right: 0; bottom: 0; width: 260px; height: 210px;
  }
  /* Back */
  .card-back { left: 388px; top: 505px; width: 567px; height: 352px; }
  .back-band { position: absolute; left: 0; right: 0; height: 93px; background: var(--brand-green); }
  .back-band.top { top: 0; }
  .back-band.bottom { bottom: 0; height: 94px; }
  .card-back .brand-name { left: 50%; top: 50%; transform: translate(-50%, -50%); font-size: 22px; }
</style>
</head>
<body>
  <section class="card card-front" aria-label="Business card front">
    <div class="front-header">
      <div class="brand-name"><span class="brand-mark"></span>Atelier Vane Architecture</div>
    </div>
    <div class="front-panel">
      <p class="contact-name">Dominic K. Whitlow</p>
      <p class="contact-credentials">AIA, NCARB, LEED AP BD+C</p>
      <ul class="contact-list">
        <li><svg viewBox="0 0 12 12"><path d="M2.5 1 4.5 1 5.3 3.6 4 4.6C4.7 6 6 7.3 7.4 8L8.4 6.7 11 7.5 11 9.5C11 10.3 10.3 11 9.5 11 5 11 1 7 1 2.5 1 1.7 1.7 1 2.5 1Z"/></svg>044-555 010 274</li>
        <li><svg viewBox="0 0 12 12"><path d="M1 3h10v6H1z M1 3l5 3.5L11 3" /></svg>hello@ateliervane.example</li>
        <li><svg viewBox="0 0 12 12"><circle cx="6" cy="6" r="5"/></svg>www.ateliervane.example</li>
      </ul>
      <p class="contact-address">742 Marbury Rd. NE Atlanta, GA 30319</p>
      <svg class="panel-accent" viewBox="0 0 260 210" role="img" aria-label="Decorative brushstroke accent in brand green">
        <path d="M0 210 C60 150 120 110 260 40 L260 210 Z" fill="var(--brand-green-soft)"/>
      </svg>
    </div>
  </section>

  <section class="card card-back" aria-label="Business card back">
    <div class="back-band top"></div>
    <div class="brand-name"><span class="brand-mark"></span>Atelier Vane Architecture</div>
    <div class="back-band bottom"></div>
  </section>
</body>
</html>
```